Ferncrest Dental, LLC business card project

Business card to be designed with current logo.
Dental office- please keep design of card that looks clean and professional.
Please include the following info:
Ferncrest Dental, LLC
Dr. Lorna Pettigrew
2871 Marlowe Street
Bethlehem, PA 18093
610-555-0193
ferncrestdental.office@examplemail.test
Hello everyone-
Reason: Just got back from overseas- will look at all designs and provide feedback. Thank you!
Reason: Polling my friends for the final selection-
thank you to all those that participated- so many talented designers!

```html
<!DOCTYPE html>
<html lang="en">
<head>
<meta charset="utf-8">
<title>Ferncrest Dental, LLC — Business Card</title>
<link rel="stylesheet" href="https://fonts.googleapis.com/css2?family=Mulish:wght@400;700&family=PT+Sans+Narrow&display=swap">
<style>
  :root {
    --stage: #e9e7e3;
    --card: #050505;
    --green: #80bc30;
    --white: #ffffff;
    --shadow: rgba(0, 0, 0, 0.35);
  }
  * { box-sizing: border-box; margin: 0; padding: 0; }
  html, body {
    width: 1200px;
    height: 900px;
    overflow: hidden;
    background: var(--stage);
  }
  .sheet {
    width: 1200px;
    height: 900px;
    display: flex;
    align-items: center;
    justify-content: center;
    gap: 40px;
  }
  .card {
    position: relative;
    width: 540px;
    height: 300px;
    background: var(--card);
    box-shadow: 0 8px 24px var(--shadow);
    display: flex;
    flex-direction: column;
    align-items: center;
  }
  .brand {
    display: flex;
    align-items: center;
    gap: 8px;
    font-family: "Mulish", sans-serif;
    font-weight: 400;
    color: var(--green);
    white-space: nowrap;
  }
  .brand-dot {
    width: 12px;
    height: 12px;
    border-radius: 50%;
    background: var(--green);
  }
  .card-front .brand {
    margin-top: 30px;
    font-size: 24px;
  }
  .doctor-name {
    margin-top: 72px;
    font-family: "Mulish", sans-serif;
    font-weight: 700;
    font-size: 23px;
    color: var(--white);
  }
  .contact-row {
    position: absolute;
    left: 0;
    right: 0;
    bottom: 26px;
    display: flex;
    justify-content: center;
    align-items: center;
    gap: 16px;
    font-family: "PT Sans Narrow", sans-serif;
    font-size: 13px;
    color: var(--green);
    white-space: nowrap;
  }
  .contact-item {
    display: flex;
    align-items: center;
    gap: 5px;
  }
  .contact-icon {
    width: 12px;
    height: 12px;
    fill: var(--green);
  }
  .at-sign {
    font-family: "Mulish", sans-serif;
    font-weight: 700;
    font-size: 14px;
    line-height: 1;
  }
  .card-back {
    justify-content: center;
  }
  .card-back .brand {
    font-size: 32px;
    gap: 10px;
  }
  .card-back .brand-dot {
    width: 16px;
    height: 16px;
  }
</style>
</head>
<body>
  <main class="sheet">
    <section class="card card-front" aria-label="Card front">
      <div class="brand"><span class="brand-dot"></span>Ferncrest Dental, LLC</div>
      <h1 class="doctor-name">Dr. Lorna Pettigrew</h1>
      <div class="contact-row">
        <span class="contact-item">
          <svg class="contact-icon" viewBox="0 0 24 24" aria-hidden="true"><path d="M12 2a7 7 0 0 0-7 7c0 5 7 13 7 13s7-8 7-13a7 7 0 0 0-7-7zm0 9.5A2.5 2.5 0 1 1 12 6.5a2.5 2.5 0 0 1 0 5z"/></svg>
          2871 Marlowe Street, Bethlehem, PA 18093
        </span>
        <span class="contact-item">
          <span class="at-sign">@</span>
          ferncrestdental.office@examplemail.test
        </span>
        <span class="contact-item">
          <svg class="contact-icon" viewBox="0 0 24 24" aria-hidden="true"><path d="M6.6 10.8a15 15 0 0 0 6.6 6.6l2.2-2.2a1 1 0 0 1 1-.25 11.4 11.4 0 0 0 3.6.57 1 1 0 0 1 1 1V20a1 1 0 0 1-1 1A17 17 0 0 1 3 4a1 1 0 0 1 1-1h3.5a1 1 0 0 1 1 1c0 1.25.2 2.45.57 3.57a1 1 0 0 1-.25 1z"/></svg>
          610-555-0193
        </span>
      </div>
    </section>

    <section class="card card-back" aria-label="Card back">
      <div class="brand"><span class="brand-dot"></span>Ferncrest Dental, LLC</div>
    </section>
  </main>
</body>
</html>
```